75%-100% OFF - Insulation Banner Design

Need banners created for an online marketing push for my insulation business Velmoor Energy.

www.velmoorenergy.com

Specifically - I would like the banners to pop utilizing our colors in neon. To see samples of colors we use - visit our asset folder.

https://files.quarnex.com/share/7hTkw29plDfa0XbmQzRv4uYc8JnG3sLe?view=open

I will attach sample files to this project.

The banner must highlight 75%-100% off Insulation and Weatherization. If you can include our current perfect Brivvo reviews somewhere in the advertisement that would be awesome but not a requirement.

The banner must meet Kettle Rebate logo guidelines. Please see attachment.

Target Market(s)

Home Owners

Industry/Entity Type

Insulation and Construction

Font styles to use
Sans Serif

Colors
59FF00
82FF00
B8FF75
E3FFCB
F4FFEA

Requirements
Must have
• Kettle Rebate Logo per project description. Must have 75-100% off somewhere that is very clear. And must have our company Velmoor Energy Logo.
Nice to have
• Velmoor Energy Logo

```html
<!DOCTYPE html>
<html lang="en">
<head>
<meta charset="utf-8">
<title>Velmoor Energy – 75%-100% Off Insulation Banner</title>
<link rel="stylesheet" href="https://fonts.googleapis.com/css2?family=Baloo+2:wght@800&family=Oswald:wght@500;600&display=swap">
<style>
  :root {
    --page-bg: #d4d4d4;
    --green-base: #1fdc55;
    --green-bright: #00e64d;
    --green-deep: #0b9a40;
    --green-glow: #c9ffd9;
    --mint: #9dffc6;
    --offer-orange: #ff6a00;
    --offer-orange-light: #ffa45a;
    --offer-blue: #1a6fdc;
    --white: #ffffff;
  }
  * { margin: 0; padding: 0; box-sizing: border-box; }
  html, body {
    width: 1200px;
    height: 610px;
    overflow: hidden;
    background: var(--page-bg);
  }
  .banner {
    position: absolute;
    left: 40px;
    top: 56px;
    width: 1120px;
    height: 497px;
    display: block;
  }
  .bg-base { fill: var(--green-base); }
  .bg-corner { fill: var(--green-deep); }
  .bg-band-bright { fill: var(--green-bright); }
  .bg-band-mint { fill: var(--mint); }
  .offer-headline {
    font-family: "Baloo 2", sans-serif;
    font-weight: 800;
    paint-order: stroke fill;
    stroke-linejoin: round;
  }
  .offer-headline-outer { fill: var(--white); stroke: var(--green-bright); stroke-width: 34; }
  .offer-headline-inner { fill: url(#orangeFill); stroke: var(--white); stroke-width: 14; }
  .offer-services {
    font-family: "Oswald", sans-serif;
    font-weight: 600;
    paint-order: stroke fill;
    stroke: var(--white);
    stroke-width: 8;
    stroke-linejoin: round;
  }
  .service-blue { fill: var(--offer-blue); }
  .service-orange { fill: var(--offer-orange); }
  .brand-name {
    font-family: "Oswald", sans-serif;
    font-weight: 500;
    fill: var(--white);
  }
  .brand-mark { fill: none; stroke: var(--white); stroke-width: 7; }
  .brand-divider { stroke: var(--white); stroke-width: 4; }
  .partner-badge { fill: var(--white); opacity: 0.9; }
</style>
</head>
<body>
<svg class="banner" viewBox="0 0 1832 813" xmlns="http://www.w3.org/2000/svg" aria-labelledby="bannerTitle">
  <title id="bannerTitle">75%-100% off insulation, weatherization and energy saving with Velmoor Energy, a Kettle Rebate partner</title>
  <defs>
    <radialGradient id="centerGlow" cx="876" cy="480" r="900" gradientUnits="userSpaceOnUse">
      <stop offset="0" stop-color="var(--green-glow)"/>
      <stop offset="0.35" stop-color="#6fec94"/>
      <stop offset="1" stop-color="var(--green-base)" stop-opacity="0"/>
    </radialGradient>
    <linearGradient id="orangeFill" x1="0" y1="0" x2="0" y2="1">
      <stop offset="0" stop-color="var(--offer-orange-light)"/>
      <stop offset="0.5" stop-color="var(--offer-orange)"/>
      <stop offset="1" stop-color="var(--offer-orange)"/>
    </linearGradient>
  </defs>

  <g class="banner-background">
    <rect class="bg-base" width="1832" height="813"/>
    <rect width="1832" height="813" fill="url(#centerGlow)" role="img" aria-label="Soft light burst glowing from the centre"/>
    <polygon class="bg-corner" points="0,0 900,0 0,130"/>
    <polygon class="bg-band-bright" points="0,130 900,0 1010,0 0,235"/>
    <polygon class="bg-band-mint" points="0,200 880,0 1000,0 0,232"/>
    <polygon class="bg-corner" points="1832,705 1832,813 1000,813"/>
    <polygon class="bg-band-bright" points="1832,560 1832,705 1000,813 900,813"/>
    <polygon class="bg-band-mint" points="1832,570 1832,600 940,813 880,813"/>
  </g>

  <g class="offer">
    <text class="offer-headline offer-headline-outer" x="316" y="430" font-size="225" textLength="1070" lengthAdjust="spacingAndGlyphs">75%-100%</text>
    <text class="offer-headline offer-headline-inner" x="316" y="430" font-size="225" textLength="1070" lengthAdjust="spacingAndGlyphs">75%-100%</text>
    <text class="offer-headline offer-headline-outer" x="1392" y="330" font-size="88" textLength="140" lengthAdjust="spacingAndGlyphs">OFF</text>
    <text class="offer-headline offer-headline-inner" x="1392" y="330" font-size="88" textLength="140" lengthAdjust="spacingAndGlyphs">OFF</text>

    <text class="offer-services" x="316" y="554" font-size="86" textLength="1240" lengthAdjust="spacingAndGlyphs"><tspan class="service-blue">INSULATION </tspan><tspan class="service-orange">WEATHERIZATION </tspan><tspan class="service-blue">ENERGY SAVING</tspan></text>
  </g>

  <g class="brand">
    <rect class="brand-mark" x="90" y="682" width="50" height="50"/>
    <text class="brand-name" x="160" y="728" font-size="54" textLength="290" lengthAdjust="spacingAndGlyphs">Velmoor Energy</text>
    <line class="brand-divider" x1="494" y1="640" x2="494" y2="780"/>
    <circle class="partner-badge" cx="676" cy="705" r="72" role="img" aria-label="Kettle Rebate partner badge"/>
  </g>
</svg>
</body>
</html>
```